Electrical company 7Kites needs a new logo design.

Need business cards for electrical company.
Modern/luxury/ Smart.
Thinking Black with White text.
Attached the logo below.

We would like two versions made - each one having different contact information on (one for each company directors). Both however will have same company address -

Fennel Court 31-35 Garwick Lane
Harwell Marsh
Kestford Vale
SS7 4PT

Contact details 1 -
Gareth Penwright
Director
gaz@7kites-demo.co.uk
07700900318

Contact details 2 -
Kieran Ashbury
Director
07700900742
kieran@7kites-demo.co.uk

Logo Text

7 Kites Electrical Solutions

```html
<!DOCTYPE html>
<html lang="en">
<head>
<meta charset="utf-8">
<title>7Kites Business Cards</title>
<link href="https://fonts.googleapis.com/css2?family=Mulish:wght@400;700&display=swap" rel="stylesheet">
<style>
  :root {
    --backdrop: #cdcdcd;
    --card: #000000;
    --gold: #c4a76a;
    --ink: #ffffff;
  }
  * { margin: 0; padding: 0; box-sizing: border-box; }
  html, body {
    width: 1200px;
    height: 1196px;
    overflow: hidden;
    background: var(--backdrop);
    font-family: "Mulish", sans-serif;
  }
  .card {
    position: absolute;
    left: 343px;
    width: 514px;
    height: 285px;
    background: var(--card);
  }
  .card--front { top: 234px; }
  .card--back { top: 669px; }

  .brand-name {
    position: absolute;
    color: var(--ink);
    font-weight: 400;
    font-size: 40px;
    letter-spacing: 1px;
    line-height: 1;
    transform: translate(-50%, -50%);
    white-space: nowrap;
  }
  .card--front .brand-name { left: 143px; top: 134px; }
  .card--back .brand-name { left: 257px; top: 140px; }

  .divider {
    position: absolute;
    left: 256px;
    top: 40px;
    width: 2px;
    height: 205px;
    background: var(--gold);
  }
  .contact {
    position: absolute;
    left: 283px;
    top: 57px;
    color: var(--ink);
    font-size: 13px;
    line-height: 15.5px;
    white-space: nowrap;
  }
  .contact__name {
    color: var(--gold);
    font-weight: 700;
    font-size: 17px;
    line-height: 20px;
  }
  .contact__role { margin-top: 1px; }
  .contact__lines { margin-top: 20px; font-size: 13.5px; line-height: 17px; }
  .contact__address { margin-top: 19px; line-height: 15.6px; }
</style>
</head>
<body>
  <section class="card card--front">
    <div class="brand-name">7Kites</div>
    <div class="divider"></div>
    <div class="contact">
      <p class="contact__name">Gareth Penwright</p>
      <p class="contact__role">Director</p>
      <div class="contact__lines">
        <p>gaz@7kites-demo.co.uk</p>
        <p>07700900318</p>
      </div>
      <div class="contact__address">
        <p>Fennel Court 31-35 Garwick Lane</p>
        <p>Harwell Marsh</p>
        <p>Kestford Vale</p>
        <p>SS7 4PT</p>
      </div>
    </div>
  </section>

  <section class="card card--back">
    <div class="brand-name">7Kites</div>
  </section>
</body>
</html>
```